Business card Zottelgarten

Business card is for a self-employed dog trainer with own dog school. Name and logo of the dog school are available. Color specifications as well. The design should be classy and minimalist, but also modern. An already existing idea would be: Front: Only the logo Back: Contact data

Font styles to use
Serif
Sans Serif
Other font styles liked:
• Trajan Pro

Colors
f78f20

Requirements
Must have
• Name: Margit Wendler-Rasch Title: Dipl. Dog Trainer Contain my logo Follow my font and color preferences (see files)

```html
<!DOCTYPE html>
<html lang="en">
<head>
<meta charset="utf-8">
<title>Zottelgarten – Business Card</title>
<link rel="stylesheet" href="https://fonts.googleapis.com/css2?family=Cinzel:wght@400;600&display=swap">
<style>
  :root {
    --stage: #2b2a2a;
    --front-bg: #70665e;
    --band: #c8842f;
    --band-text: #f3cf6e;
    --logo-white: #f4f2f0;
    --back-bg: #cbc5c2;
    --back-faint: #9e9792;
    --divider: #a49d98;
    --label: #e08a22;
    --ink: #3a3431;
  }
  * { margin: 0; padding: 0; box-sizing: border-box; }
  html, body {
    width: 1200px; height: 800px; overflow: hidden;
    background: var(--stage);
    font-family: "Cinzel", serif;
  }
  .stage {
    width: 1200px; height: 800px;
    display: flex; align-items: center; justify-content: center; gap: 50px;
  }
  .card {
    width: 540px; height: 340px; border-radius: 10px;
    position: relative; overflow: hidden;
    box-shadow: 0 12px 30px rgba(0,0,0,.45);
  }

  /* Front */
  .card-front { background: var(--front-bg); display: flex; }
  .role-band {
    width: 150px; height: 100%; background: var(--band);
    display: flex; align-items: center; justify-content: center;
  }
  .role-band__text {
    transform: rotate(-90deg); white-space: nowrap;
    color: var(--band-text); font-size: 26px; letter-spacing: 2px;
  }
  .front-brand {
    flex: 1; display: flex; flex-direction: column; align-items: center; justify-content: center;
    color: var(--logo-white); padding-top: 10px;
  }
  .brand-circle {
    width: 112px; height: 112px; border-radius: 50%;
    background: var(--logo-white); margin-bottom: 12px;
  }
  .brand-name { font-size: 34px; letter-spacing: 2px; line-height: 1; }
  .brand-url { font-size: 11px; letter-spacing: 6px; margin-top: 4px; }

  /* Back */
  .card-back { background: var(--back-bg); display: flex; }
  .back-brand {
    width: 50%; display: flex; flex-direction: column; align-items: center; justify-content: center;
    color: var(--back-faint); padding-bottom: 40px;
  }
  .back-brand .brand-circle { background: var(--back-faint); width: 96px; height: 96px; opacity: .7; }
  .back-brand .brand-name { font-size: 28px; }
  .back-brand .brand-url { font-size: 9px; letter-spacing: 5px; }
  .back-divider { width: 2px; background: var(--divider); }
  .contact {
    flex: 1; padding: 120px 0 0 26px;
    font-size: 12px; color: var(--ink); letter-spacing: .5px; line-height: 2;
  }
  .contact__label { color: var(--label); font-weight: 600; }
</style>
</head>
<body>
<main class="stage">
  <section class="card card-front">
    <div class="role-band"><span class="role-band__text">Dog Trainer</span></div>
    <div class="front-brand">
      <div class="brand-circle"></div>
      <div class="brand-name">ZOTTELGARTEN</div>
      <div class="brand-url">WWW.ZOTTELGARTEN.CH</div>
    </div>
  </section>

  <section class="card card-back">
    <div class="back-brand">
      <div class="brand-circle"></div>
      <div class="brand-name">ZOTTELGARTEN</div>
      <div class="brand-url">WWW.ZOTTELGARTEN.CH</div>
    </div>
    <div class="back-divider"></div>
    <div class="contact">
      <p><span class="contact__label">Name</span> : Margit Wendler-Rasch</p>
      <p><span class="contact__label">Title</span> : Dipl. Dog Trainer</p>
    </div>
  </section>
</main>
</body>
</html>
```